Aquafresh A5 mailer

To design a A5 mailing postcard (two sided) to promote out Wet Cleaning service to new 'Dry Cleaning' shops & businesses.

We supply the Tovaro & Bellonti laundry equipment to facilitate the process which is a replacement to the traditional Dry Cleaning wash process.

The examples of designs attached are ones we have done before ourselves but are not suitable for postcard format.

Target Market(s)

Dry Cleaning shops & businesses

Industry/Entity Type

Cleaning Service

Requirements
Must have
• Compatibility with mailing template attached. Must be two sided. We could include some generic information about Harlow Electrics on the address side, if everything else fits on the front.

```html
<!DOCTYPE html>
<html lang="en">
<head>
<meta charset="utf-8">
<title>Wet Cleaning Mailer</title>
<link href="https://fonts.googleapis.com/css2?family=Lato:wght@300;400;700;900&family=Oswald:wght@500&display=swap" rel="stylesheet">
<style>
  :root {
    --backdrop: #4a4a4a;
    --royal: #3a52a6;
    --navy: #2c3d8f;
    --red: #e3242b;
    --white: #ffffff;
    --ink: #1f1f1f;
    --photo-warm: #c9b8a6;
    --photo-cool: #b9c6d8;
  }
  * { margin: 0; padding: 0; box-sizing: border-box; }
  html, body { width: 907px; height: 1200px; overflow: hidden; background: var(--backdrop); }
  body { position: relative; font-family: "Lato", sans-serif; }

  .card { position: absolute; background: var(--white); overflow: hidden; }
  .card-front { left: 66px; top: 52px; width: 772px; height: 520px; }
  .card-back { left: 66px; top: 617px; width: 777px; height: 543px; }
  .card-shapes { position: absolute; inset: 0; }

  .photo { position: absolute; border-radius: 50%; }
  .photo-laundry { left: 16px; top: 45px; width: 230px; height: 230px; border: 4px solid var(--red);
    background: radial-gradient(circle at 45% 55%, #d7c4ae, var(--photo-warm) 60%, #9fb3cc); }
  .photo-washer { left: 125px; top: 220px; width: 164px; height: 164px; border: 4px solid var(--navy);
    background: radial-gradient(circle at 40% 55%, #eef0f3, var(--photo-cool) 70%); }

  .front-question { position: absolute; left: 314px; top: 42px; color: var(--white); font-size: 16.5px; }
  .front-headline { position: absolute; left: 314px; top: 72px; color: var(--red);
    font-family: "Oswald", sans-serif; font-weight: 500; font-size: 29px; letter-spacing: -0.4px; line-height: 40px; }
  .front-body { position: absolute; left: 315px; top: 140px; width: 434px; color: var(--ink);
    font-size: 17px; line-height: 21px; text-align: justify; }
  .front-body p + p { margin-top: 21px; }

  .front-title { position: absolute; left: 66px; top: 406px; color: var(--white); line-height: 46px; }
  .front-title strong { display: block; font-weight: 700; font-size: 44px; }
  .front-title span { display: block; font-weight: 300; font-size: 43px; }

  .brand-name { position: absolute; left: 590px; top: 443px; color: var(--white);
    font-weight: 900; font-size: 21px; display: flex; align-items: center; gap: 8px; }
  .brand-name::before { content: ""; width: 14px; height: 14px; background: var(--red); }

  .offer { position: absolute; left: 24px; top: 40px; width: 352px; color: var(--white); font-size: 14.5px; line-height: 18px; }
  .offer .price { color: var(--red); font-weight: 900; font-size: 27px; }
  .offer p + p { margin-top: 8px; }

  .section-tab { position: absolute; left: 0; top: 170px; width: 187px; height: 44px; background: var(--red);
    border-radius: 0 22px 22px 0; color: var(--white); font-weight: 700; font-size: 30px; line-height: 44px; padding-left: 33px; }
  .about-text { position: absolute; left: 24px; top: 232px; width: 336px; color: var(--white); font-size: 14.5px; line-height: 17.8px; }

  .contact { position: absolute; left: 32px; top: 413px; width: 332px; height: 81px; background: var(--white);
    border-radius: 30px; text-align: center; color: var(--ink); padding-top: 6px; }
  .contact-lead, .contact-tail { font-weight: 700; font-size: 15px; line-height: 18px; }
  .contact-phone { color: var(--red); font-weight: 900; font-size: 34px; line-height: 36px; }

  .stamp-box { position: absolute; left: 668px; top: 99px; width: 61px; height: 65px; border: 1.5px solid #333; }
  .address-line { position: absolute; left: 450px; width: 283px; height: 1.5px; background: #444; }
</style>
</head>
<body>

  <section class="card card-front">
    <svg class="card-shapes" width="772" height="520" viewBox="0 0 772 520">
      <path fill="var(--navy)" d="M0 0H772V92H330C300 92 292 60 270 40C250 20 200 12 140 12H0Z"/>
      <path fill="var(--royal)" d="M0 520V440C120 360 230 330 330 335C470 345 560 395 640 392C700 390 740 370 772 352V520Z"/>
      <path fill="var(--red)" d="M520 386C620 404 720 380 772 290V312C730 392 630 410 520 386Z"/>
      <path fill="var(--navy)" d="M0 440C120 360 230 326 330 332C260 336 120 380 0 458Z"/>
      <circle cx="94" cy="286" r="17" fill="var(--navy)"/>
      <circle cx="58" cy="290" r="7" fill="var(--navy)"/>
      <circle cx="248" cy="209" r="8" fill="var(--navy)"/>
      <circle cx="710" cy="360" r="23" fill="var(--navy)"/>
      <circle cx="669" cy="342" r="10" fill="var(--navy)"/>
    </svg>
    <div class="photo photo-laundry" role="img" aria-label="Photo of a laundry basket of colourful clothes beside an iron"></div>
    <div class="photo photo-washer" role="img" aria-label="Photo of a woman loading a front-loading washing machine"></div>

    <p class="front-question">Worried about the health implications surrounding PERC?</p>
    <h2 class="front-headline">Want a safer Wet Cleaning environment?</h2>
    <div class="front-body">
      <p>Why not have the latest in Wetvora commercial laundry equipment, Bellonti Finishing equipment and the safe Kestrane chemicals installed to achieve the very best results in a totally safe environment.</p>
      <p>Wet Cleaning machines will allow you to wash the very same items you currently put in your dry cleaning machine, from suits, to wedding dresses and even suede's and leathers!</p>
    </div>
    <h1 class="front-title"><strong>Wet Cleaning</strong><span>The new safer concept</span></h1>
    <div class="brand-name">Harlow Electrics</div>
  </section>

  <section class="card card-back">
    <svg class="card-shapes" width="777" height="543" viewBox="0 0 777 543">
      <path fill="var(--royal)" d="M0 0H372C400 60 400 140 378 220C356 310 350 420 420 543H0Z"/>
      <path fill="var(--navy)" d="M372 0H392C425 70 418 150 396 230C372 320 372 430 430 543H420C350 420 356 310 378 220C400 140 400 60 372 0Z"/>
      <path fill="var(--red)" d="M360 390C355 450 380 500 430 543H460C400 500 372 450 368 390Z"/>
      <circle cx="330" cy="22" r="20" fill="#b4bde0"/>
      <circle cx="297" cy="37" r="7" fill="#b4bde0"/>
      <circle cx="338" cy="373" r="16" fill="#b4bde0"/>
      <circle cx="307" cy="393" r="28" fill="#8f9ccf"/>
    </svg>
    <div class="offer">
      <p>From only <span class="price">£999</span> a month you could become a Wet Cleaning Specialist.</p>
      <p>The package will include the Wet Cleaning washer and dryer, trouser topper, body former, finishing table and boiler on a fully maintained agreement.</p>
    </div>
    <h2 class="section-tab">About Us</h2>
    <p class="about-text">Lorem ipsum dolor sit amet, consectetuer adipiscing elit, sed diam nonummy nibh euismod tincidunt ut laoreet dolore magna aliquam erat volutpat. Ut wisi enim ad minim veniam, quis nostrud exercitation ullamcorper suscipit lobortis nisl ut aliquip ex ea commodo consequat. Duis autem vel eum iriure dolor in hendrerit in vulputate velit esse molestie consequat, vel illum dolore eu feugiat nulla facilisis at vero eros et accumsan</p>
    <div class="contact">
      <p class="contact-lead">Please contact Harlow Electrics on</p>
      <p class="contact-phone">0116 496 0321</p>
      <p class="contact-tail">to discuss this further</p>
    </div>
    <div class="stamp-box"></div>
    <div class="address-line" style="top:328px"></div>
    <div class="address-line" style="top:361px"></div>
    <div class="address-line" style="top:396px"></div>
  </section>

</body>
</html>
```